FR banner

we need a banner design (36"x120" horizontal) that will be displayed on a local high school baseball field. My company ( Crestwell Prints Co) has been producing signage for the Fernmoor Ridge community since 2009. We would like to communicate that we do more than banners. The final design should include the slogan "Signs Shirts Swag" and our Logo.

Target Market(s)

companies, teams, events, shirt and other marketing items.

Industry/Entity Type

Sign, Print,

Font styles to use
Sans Serif

Requirements
Should not have
• no baseball content.

```html
<!DOCTYPE html>
<html lang="en">
<head>
<meta charset="utf-8">
<title>Crestwell Prints Co — Signs Shirts Swag Banner</title>
<link rel="stylesheet" href="https://fonts.googleapis.com/css2?family=Playfair+Display:wght@700;900&display=swap">
<style>
  :root {
    --brand-navy: #444b8f;
    --leaf-white: #ffffff;
    --leaf-mist: #e6eaf5;
    --leaf-sky: #b1c2e1;
    --ring-cyan: #6cc3df;
    --ink-black: #111111;
    --type-white: #ffffff;
  }
  html, body {
    margin: 0;
    padding: 0;
    overflow: hidden;
    background: #ffffff;
  }
  .banner {
    position: relative;
    width: 1200px;
    height: 360px;
    background: var(--brand-navy);
    overflow: hidden;
    font-family: "Playfair Display", Georgia, serif;
  }
  .banner__swoosh {
    position: absolute;
    inset: 0;
  }
  .banner__photo {
    position: absolute;
    left: 66px;
    top: 22px;
    width: 306px;
    height: 306px;
    border-radius: 50%;
    border: 6px solid var(--ring-cyan);
    background:
      linear-gradient(160deg, #e9eef8 0%, #c9d0dc 28%, transparent 29%),
      linear-gradient(200deg, #f4e12a 0%, #ee2f86 30%, #2fa9dd 55%, #1b1b1f 85%);
  }
  .banner__brand {
    position: absolute;
    left: 596px;
    top: 112px;
    transform: translate(-50%, -50%);
    margin: 0;
    font-weight: 900;
    font-size: 26px;
    color: var(--ink-black);
    white-space: nowrap;
  }
  .banner__slogan {
    position: absolute;
    right: 33px;
    top: 22px;
    margin: 0;
    text-align: right;
    font-weight: 900;
    font-size: 96px;
    line-height: 89px;
    color: var(--type-white);
    text-transform: uppercase;
  }
  .banner__slogan span { display: block; }
  .banner__tagline {
    position: absolute;
    right: 33px;
    top: 304px;
    margin: 0;
    font-weight: 700;
    font-size: 26px;
    letter-spacing: 3.2px;
    color: var(--type-white);
    text-transform: uppercase;
    white-space: nowrap;
  }
</style>
</head>
<body>
  <div class="banner">
    <svg class="banner__swoosh" width="1200" height="360" viewBox="0 0 1200 360" aria-hidden="true">
      <path d="M20 343 C 200 150, 500 20, 792 0 C 700 220, 400 320, 20 343 Z" fill="var(--leaf-sky)"/>
      <path d="M20 343 C 200 170, 480 40, 740 8 C 680 200, 400 312, 20 343 Z" fill="var(--leaf-mist)"/>
      <path d="M20 343 C 220 190, 480 80, 735 65 C 660 225, 400 318, 20 343 Z" fill="var(--leaf-white)"/>
    </svg>

    <div class="banner__photo" role="img" aria-label="Wide-format printer laying down bands of yellow, magenta, cyan and black ink"></div>

    <p class="banner__brand">Crestwell Prints Co</p>

    <h1 class="banner__slogan">
      <span>Signs</span>
      <span>Shirts</span>
      <span>Swag</span>
    </h1>

    <p class="banner__tagline">Fernmoor Ridge Community Since 2009</p>
  </div>
</body>
</html>
```